Vexpad Business Card design needed

I want to have my new business card designed to look like the Vexpad lock screen. The front will contain my logo but just the (B) design not all the wording (attached) in the center of the card(screen) and the slide to unlock will be pointer in orange and then Brelow Insurance Inc. Not sure about the rest of the front of the card. Guessing some random date and the service bars I will leave up to your creative minds to come up with some cool. I am an insurance agency. For the back of the card I want it to look like a contact within an Vexpad (picture and contact information,address etc..) I think you get the point. My name is Dale Brelow. Cell is 555-203-7718 Office 555-610-4927 (fax number is (555) 284-0196 address is UPDATE Website is www.brelowinsurance.com.

If you not sure what I am looking for finderly Vexpad business card images or see samples I uploaded.

Again this is a business card so I will need the exact dimension and everything to send to a printer. File must be PRINT ready so please make sure it has smooth edges(no buttons on side of Vexpad)

New Address is 
2718 Marlowe Bend
Suite 410
Indianapolis
IN
46917

Please use this in your design.

email that needs to go on card is Dale@brelowinsurance.com If you are submitting designs please make sure it is new ux4 update design for the Vexpad.

Reason: Need to extend for a few days.

Industry/Entity Type

Insurance

Requirements
Must have
• I am open to seeing designs with the font provide along with the standard Vexpad font. Must use my colors. I would like to see designs with the standard Vexpad contact colors but also with my colors. Have fun with the design if you can. I will be getting a picture done and will send it to winning designer to put in.
Should not have
• Do not want a standard square card. Make it look like an Vexpad 3 shape please. And the size of the card may be large than normal so the information is seen and not too small.

```html
<!DOCTYPE html>
<html lang="en">
<head>
<meta charset="utf-8">
<title>Brelow Insurance – Vexpad Card</title>
<link rel="stylesheet" href="https://fonts.googleapis.com/css2?family=Roboto:wght@100;300;400;500&display=swap">
<style>
  :root {
    --page: #ffffff;
    --frame: #141414;
    --screen-white: #ffffff;
    --ink: #111111;
    --link-blue: #2f7fd8;
    --tab-dark: #1e1e1e;
    --tab-light: #3a3a3a;
    --tab-icon: #e8e8e8;
    --brand-orange: #f26a1f;
    --lock-top: #4a5459;
    --lock-mid: #2c3439;
    --lock-bottom: #171c1f;
    --lock-text: #ffffff;
    --slider-track: #e9e9e9;
    --slider-text: #2a2a2a;
  }
  * { box-sizing: border-box; margin: 0; padding: 0; }
  html, body { width: 1200px; height: 940px; overflow: hidden; background: var(--page); }
  body { position: relative; font-family: "Roboto", sans-serif; color: var(--ink); }

  .device {
    position: absolute;
    background: var(--frame);
    border-radius: 18px;
    overflow: hidden;
  }
  .device--contact { left: 25px; top: 18px; width: 595px; height: 910px; padding: 10px; }
  .device--lock { left: 652px; top: 18px; width: 536px; height: 910px; padding: 10px; }

  /* ---------- contact side ---------- */
  .contact-screen {
    position: relative; width: 100%; height: 100%;
    background: var(--screen-white); border-radius: 8px; overflow: hidden;
  }
  .status-bar {
    position: absolute; left: 0; right: 0; top: 0; height: 40px;
    display: flex; align-items: center; justify-content: space-between;
    padding: 0 18px; font-size: 16px;
  }
  .status-bar__signal { display: flex; gap: 4px; align-items: center; }
  .status-bar__dot { width: 9px; height: 9px; border-radius: 50%; background: currentColor; }
  .status-bar__right { display: flex; align-items: center; gap: 6px; }
  .battery { width: 34px; height: 14px; border: 1.5px solid currentColor; border-radius: 3px; padding: 1.5px; }
  .battery__fill { width: 100%; height: 100%; background: currentColor; border-radius: 1px; }
  .status-bar--dark { color: var(--ink); }
  .status-bar--light { color: var(--lock-text); }

  .nav-bar {
    position: absolute; left: 18px; right: 24px; top: 44px;
    display: flex; justify-content: space-between; color: var(--link-blue); font-size: 15px;
  }

  .contact-header { position: absolute; left: 45px; top: 112px; display: flex; align-items: center; gap: 40px; }
  .avatar {
    width: 92px; height: 92px; border-radius: 50%; background: var(--ink);
    color: #fff; display: flex; align-items: center; justify-content: center; font-size: 15px;
  }
  .contact-name { font-size: 32px; font-weight: 400; line-height: 1.25; }
  .contact-company { font-size: 30px; font-weight: 300; line-height: 1.2; }

  .field-list { position: absolute; left: 92px; top: 262px; width: 420px; }
  .field { position: relative; margin-bottom: 8px; }
  .field__label { color: var(--link-blue); font-size: 24px; line-height: 1.1; }
  .field__value { font-size: 24px; line-height: 1.2; }
  .field__icon { position: absolute; right: -4px; top: 8px; width: 26px; height: 26px; }

  .tab-bar {
    position: absolute; left: 0; right: 0; bottom: 0; height: 118px;
    background: linear-gradient(var(--tab-light), var(--tab-dark));
    display: flex; justify-content: space-around; align-items: center; padding-top: 8px;
  }
  .tab { display: flex; flex-direction: column; align-items: center; color: var(--tab-icon); font-size: 22px; }
  .tab svg { width: 52px; height: 52px; margin-bottom: 4px; }

  /* ---------- lock side ---------- */
  .lock-screen {
    position: relative; width: 100%; height: 100%; border-radius: 8px; overflow: hidden;
    background: radial-gradient(ellipse at 50% 30%, var(--lock-top), var(--lock-mid) 60%, var(--lock-bottom));
    color: var(--lock-text);
  }
  .lock-wallpaper { position: absolute; inset: 0; background: radial-gradient(ellipse at 50% 30%, var(--lock-top), var(--lock-mid) 60%, var(--lock-bottom)); }
  .lock-clock { position: absolute; left: 0; right: 0; top: 58px; text-align: center; font-size: 92px; font-weight: 100; line-height: 1; }
  .lock-date { position: absolute; left: 0; right: 0; top: 162px; text-align: center; font-size: 20px; font-weight: 300; }
  .lock-brand {
    position: absolute; left: 0; right: 0; top: 340px; text-align: center;
    font-size: 96px; font-weight: 300; color: var(--brand-orange); letter-spacing: 1px;
  }
  .slider {
    position: absolute; left: 20px; right: 20px; bottom: 24px; height: 84px;
    background: var(--slider-track); border-radius: 6px;
    display: flex; align-items: center; gap: 36px; padding: 8px;
  }
  .slider__knob {
    width: 108px; height: 66px; background: #fff; border-radius: 6px;
    box-shadow: 0 1px 3px rgba(0,0,0,.35);
    display: flex; align-items: center; justify-content: center;
  }
  .slider__label { font-size: 34px; font-weight: 300; color: var(--slider-text); }
</style>
</head>
<body>

<section class="device device--contact" aria-label="Contact card side">
  <div class="contact-screen">
    <div class="status-bar status-bar--dark">
      <div class="status-bar__signal">
        <span class="status-bar__dot"></span><span class="status-bar__dot"></span><span class="status-bar__dot"></span><span class="status-bar__dot"></span><span class="status-bar__dot"></span>
      </div>
      <div class="status-bar__right"><span>100%</span><span class="battery"><span class="battery__fill"></span></span></div>
    </div>
    <div class="nav-bar"><span>‹ All Contacts</span><span>Edit</span></div>

    <header class="contact-header">
      <div class="avatar">PIC</div>
      <div>
        <h1 class="contact-name">Dale Brelow</h1>
        <p class="contact-company">Brelow Insurance Inc.</p>
      </div>
    </header>

    <div class="field-list">
      <div class="field">
        <div class="field__label">work</div>
        <div class="field__value">(555) 610-4927</div>
        <svg class="field__icon" viewBox="0 0 24 24" fill="none" stroke="#2f7fd8" stroke-width="1.6"><path d="M6 3l3 4-2 2c1 3 3 5 6 6l2-2 4 3-2 3C10 19 5 14 3 5z"/></svg>
      </div>
      <div class="field">
        <div class="field__label">mobile</div>
        <div class="field__value">(555) 203-7718</div>
        <svg class="field__icon" viewBox="0 0 24 24" fill="none" stroke="#2f7fd8" stroke-width="1.6"><path d="M6 3l3 4-2 2c1 3 3 5 6 6l2-2 4 3-2 3C10 19 5 14 3 5z"/></svg>
      </div>
      <div class="field">
        <div class="field__label">fax</div>
        <div class="field__value">(555) 284-0196</div>
        <svg class="field__icon" viewBox="0 0 24 24" fill="none" stroke="#2f7fd8" stroke-width="1.6"><path d="M6 3l3 4-2 2c1 3 3 5 6 6l2-2 4 3-2 3C10 19 5 14 3 5z"/></svg>
      </div>
      <div class="field">
        <div class="field__label">email</div>
        <div class="field__value">Dale@brelowinsurance.com</div>
      </div>
      <div class="field">
        <div class="field__label">home</div>
        <div class="field__value">2718 Marlowe Bend<br>Suite 410 Indianapolis<br>IN 46917</div>
      </div>
      <div class="field">
        <div class="field__label">web</div>
        <div class="field__value">www.brelowinsurance.com</div>
        <svg class="field__icon" style="top:30px" viewBox="0 0 24 24" fill="none" stroke="#2f7fd8" stroke-width="1.6"><circle cx="12" cy="12" r="9"/><ellipse cx="12" cy="12" rx="4" ry="9"/><path d="M3 12h18M5 7h14M5 17h14"/></svg>
      </div>
    </div>

    <nav class="tab-bar">
      <div class="tab">
        <svg viewBox="0 0 24 24" fill="currentColor"><path d="M12 2l3 7h7l-5.6 4.3 2.1 7.2L12 16.3l-6.5 4.2 2.1-7.2L2 9h7z"/></svg>auto
      </div>
      <div class="tab">
        <svg viewBox="0 0 24 24" fill="none" stroke="currentColor" stroke-width="2"><circle cx="12" cy="12" r="9.5"/><path d="M12 6v6h5"/></svg>home
      </div>
      <div class="tab">
        <svg viewBox="0 0 24 24" fill="currentColor"><circle cx="12" cy="8" r="5"/><path d="M2 23c0-6 4.5-9 10-9s10 3 10 9z"/></svg>contacts
      </div>
      <div class="tab">
        <svg viewBox="0 0 24 24" fill="currentColor"><rect x="2" y="2" width="5.5" height="5.5"/><rect x="9.25" y="2" width="5.5" height="5.5"/><rect x="16.5" y="2" width="5.5" height="5.5"/><rect x="2" y="9.25" width="5.5" height="5.5"/><rect x="9.25" y="9.25" width="5.5" height="5.5"/><rect x="16.5" y="9.25" width="5.5" height="5.5"/><rect x="2" y="16.5" width="5.5" height="5.5"/><rect x="9.25" y="16.5" width="5.5" height="5.5"/><rect x="16.5" y="16.5" width="5.5" height="5.5"/></svg>life
      </div>
      <div class="tab">
        <svg viewBox="0 0 24 24" fill="none" stroke="currentColor" stroke-width="2.4"><circle cx="6" cy="13" r="4"/><circle cx="18" cy="13" r="4"/><path d="M6 17h12"/></svg>business
      </div>
    </nav>
  </div>
</section>

<section class="device device--lock" aria-label="Lock screen side">
  <div class="lock-screen">
    <div class="lock-wallpaper" role="img" aria-label="Dark grey wallpaper with water droplets"></div>
    <div class="status-bar status-bar--light">
      <div class="status-bar__signal">
        <span class="status-bar__dot"></span><span class="status-bar__dot"></span><span class="status-bar__dot"></span><span class="status-bar__dot"></span><span class="status-bar__dot"></span>
      </div>
      <div class="status-bar__right"><span>100%</span><span class="battery"><span class="battery__fill"></span></span></div>
    </div>
    <div class="lock-clock">9:32</div>
    <div class="lock-date">Monday, June 10</div>
    <div class="lock-brand">brelow</div>
    <div class="slider">
      <div class="slider__knob">
        <svg width="46" height="26" viewBox="0 0 46 26"><path d="M2 9h26V2l16 11-16 11v-7H2z" fill="#f26a1f"/></svg>
      </div>
      <span class="slider__label">brelow insurance</span>
    </div>
  </div>
</section>

</body>
</html>
```